Rack card for a integrative medical practice

Need an eye-catching rack card with our logo with content as provided. We have a membership based holistic medical practice which incorporates western and holistic medicine. We would like to focus on wellness and healthy lifestyle. See uploaded files for what is included in the membership. Would like 2 page rack card color on both sides. Logo must be on the front.

Target Market(s)

People looking for alternative medicine, healthy lifestyle.

Industry/Entity Type

Health and Wellness

Colors
00AB8E
00BBA5
67D7C9
C6EFE9
E9F9F6

Requirements
Must have
• Must spark interest at first sight. Clear message.
Nice to have
• Warm, bright and positive vibe. Organic, neutral and earthy colors.
Should not have
• Traditional medical practice vibe (cold, formal, industrial). No PINK except the logo.

```html
<!DOCTYPE html>
<html lang="en">
<head>
<meta charset="utf-8">
<title>Willow Health &amp; Wellness – Rack Card</title>
<link rel="stylesheet" href="https://fonts.googleapis.com/css2?family=Fira+Sans:wght@400;500;600&family=Lobster&display=swap">
<style>
  :root {
    --teal-deep: #00ab8e;
    --teal: #00bba5;
    --teal-light: #67d7c9;
    --mint: #c6efe9;
    --mint-pale: #e9f9f6;
    --ink-teal: #13705e;
    --ink: #1f2a2a;
    --board: #f0f0f0;
    --white: #ffffff;
  }
  * { margin: 0; padding: 0; box-sizing: border-box; }
  html, body { width: 900px; height: 1200px; overflow: hidden; }
  body {
    background: var(--board);
    font-family: "Fira Sans", Arial, sans-serif;
    color: var(--ink);
    position: relative;
  }
  .card {
    position: absolute;
    background: var(--white);
    overflow: hidden;
    box-shadow: -8px 10px 14px rgba(0,0,0,0.28);
  }
  .card-art { position: absolute; inset: 0; width: 100%; height: 100%; }

  /* Front */
  .card-front { left: 60px; top: 44px; width: 370px; height: 898px; }
  .brand {
    position: absolute; left: 24px; top: 62px;
    display: flex; align-items: center; gap: 8px;
    font-weight: 500; font-size: 20px; letter-spacing: 3px;
    color: var(--ink-teal);
  }
  .brand-dot { width: 14px; height: 14px; border-radius: 50%; background: var(--ink-teal); }
  .headline {
    position: absolute; left: 18px; top: 148px;
    font-family: "Lobster", cursive;
    font-weight: 400; font-size: 47px; line-height: 60px;
    color: var(--ink-teal);
  }
  .tagline {
    position: absolute; left: 20px; top: 350px; width: 215px;
    font-size: 14.5px; line-height: 19px; color: var(--ink);
  }

  /* Back */
  .card-back { left: 500px; top: 207px; width: 340px; height: 826px; }
  .benefits-title {
    position: absolute; left: 15px; top: 54px;
    font-size: 15px; line-height: 20px; font-weight: 600;
    color: var(--ink-teal);
  }
  .benefits {
    position: absolute; left: 15px; top: 112px;
    list-style: none;
    font-size: 12.5px; line-height: 16.5px; color: var(--ink);
  }
  .benefits li { position: relative; padding-left: 13px; width: 175px; margin-bottom: 4px; }
  .benefits li::before {
    content: ""; position: absolute; left: 0; top: 6px;
    width: 5px; height: 5px; border-radius: 50%; background: var(--ink-teal);
  }
  .benefits li.mid { width: 235px; }
  .benefits li.wide { width: 305px; }
  .address-bar {
    position: absolute; left: 0; right: 0; top: 768px; height: 42px;
    background: rgba(0,140,115,0.45);
    display: flex; align-items: center; justify-content: center;
    font-size: 13px; color: var(--mint-pale);
  }

  .side-label {
    position: absolute; font-size: 40px; font-weight: 500; color: #111;
  }
  .label-front { left: 180px; top: 990px; }
  .label-back { left: 643px; top: 1060px; }
</style>
</head>
<body>

<section class="card card-front">
  <svg class="card-art" viewBox="0 0 370 898" aria-hidden="false">
    <defs>
      <radialGradient id="flowerTone" cx="50%" cy="22%" r="60%">
        <stop offset="0" stop-color="#f2c24a"/>
        <stop offset="0.18" stop-color="#fbf6e8"/>
        <stop offset="0.55" stop-color="#eef4e6"/>
        <stop offset="1" stop-color="#ffffff" stop-opacity="0"/>
      </radialGradient>
      <linearGradient id="photoTone" x1="0" y1="0" x2="1" y2="1">
        <stop offset="0" stop-color="#e8dcd4"/>
        <stop offset="0.45" stop-color="#f4efea"/>
        <stop offset="0.75" stop-color="#c9a78f"/>
        <stop offset="1" stop-color="#a8485a"/>
      </linearGradient>
    </defs>
    <rect class="flower-photo" x="180" y="88" width="185" height="360" fill="url(#flowerTone)" role="img" aria-label="Photo of a white daisy on a long green stem"/>
    <rect class="wellness-photo" x="0" y="600" width="370" height="298" fill="url(#photoTone)" role="img" aria-label="Photo of a person in white clothing meditating cross-legged among cushions"/>
    <g class="wave-bands">
      <path d="M0 430 C130 462 260 400 370 300 L370 640 C250 650 120 620 0 600 Z" fill="var(--mint)"/>
      <path d="M0 455 C140 485 260 440 370 392 L370 620 C250 640 110 610 0 580 Z" fill="var(--teal-light)"/>
      <path d="M0 462 C150 480 280 470 370 452 L370 600 C240 640 120 600 0 540 Z" fill="var(--teal)"/>
      <path d="M0 500 C160 520 290 500 370 500 L370 560 C250 560 120 540 0 520 Z" fill="var(--mint)" opacity="0.7"/>
      <path d="M0 520 C150 545 280 530 370 530 L370 640 C260 650 120 630 0 600 Z" fill="var(--teal-deep)"/>
      <path d="M0 545 C120 590 250 600 370 610 L370 660 C230 660 100 630 0 600 Z" fill="var(--teal-light)" opacity="0.85"/>
      <path d="M0 600 C120 640 250 650 370 660 L370 690 C230 690 100 670 0 640 Z" fill="var(--mint)" opacity="0.8"/>
    </g>
  </svg>
  <div class="brand"><span class="brand-dot"></span>WILLOW</div>
  <h1 class="headline">Willow<br>Health &amp;<br>Wellness</h1>
  <p class="tagline">A direct primary care practice focused on a more Holistic and Personal approach to medicine.</p>
</section>

<section class="card card-back">
  <svg class="card-art" viewBox="0 0 340 826">
    <defs>
      <linearGradient id="leafTone" x1="0" y1="0" x2="1" y2="1">
        <stop offset="0" stop-color="#cfe8dc"/>
        <stop offset="0.5" stop-color="#5fae86"/>
        <stop offset="1" stop-color="#d9efe4"/>
      </linearGradient>
      <linearGradient id="sprigTone" x1="0" y1="1" x2="1" y2="0">
        <stop offset="0" stop-color="#4d8f72"/>
        <stop offset="1" stop-color="#c8ddd2"/>
      </linearGradient>
    </defs>
    <rect class="leaf-art" x="185" y="0" width="155" height="310" rx="60" fill="url(#leafTone)" opacity="0.75" role="img" aria-label="Watercolour illustration of monstera leaves"/>
    <rect class="sprig-art" x="160" y="385" width="160" height="125" rx="50" fill="url(#sprigTone)" opacity="0.5" role="img" aria-label="Watercolour illustration of eucalyptus sprigs"/>
    <g class="wave-bands">
      <path d="M0 430 C110 500 230 520 340 540 L340 826 L0 826 Z" fill="var(--teal-light)"/>
      <path d="M0 455 C110 540 230 570 340 580 L340 826 L0 826 Z" fill="var(--mint)" opacity="0.8"/>
      <path d="M0 480 C100 560 220 600 340 600 L340 826 L0 826 Z" fill="var(--teal)"/>
      <path d="M0 530 C120 600 230 620 340 640 L340 826 L0 826 Z" fill="var(--teal-light)" opacity="0.8"/>
      <path d="M0 585 C120 620 240 650 340 670 L340 826 L0 826 Z" fill="var(--teal-deep)"/>
    </g>
    <circle class="faint-mark" cx="168" cy="690" r="58" fill="var(--ink-teal)" opacity="0.12"/>
  </svg>
  <h2 class="benefits-title">WHAT'S INCLUDED IN<br>YOUR MEMBERSHIP :</h2>
  <ul class="benefits">
    <li>Unlimited office visits with no copay</li>
    <li>Direct communication with your doctor</li>
    <li>Discounted labs, imaging and medications</li>
    <li>Free initial acupuncture session ($250 value).</li>
    <li>2 BodyScan testings per year ($100 value)</li>
    <li class="mid">Discounts for supplements and health products in the clinic</li>
    <li class="wide">Discounts for iv vitamin infusion therapy</li>
    <li class="wide">Personalized nutrition plan after advanced testing such as gut microbiome, hormonal, metabolism test, etc.</li>
  </ul>
  <div class="address-bar">1420 Elm Park Rd., STE 2B, Riverton</div>
</section>

<p class="side-label label-front">Front</p>
<p class="side-label label-back">back</p>

</body>
</html>
```